Lumora Dwellings

Design a stylish Business card- we would like a businness card design that suits plastic business cards. Our card needs to show that we are tech savy and technology based so the design is crucial.

Target Market(s)

22-40

Industry/Entity Type

Plastic

Requirements
Must have
• attached is our logo. also double sided card would be nice.
my details

Tobias Fenwright
Director
0471596234
www.lumoradwellings.com.au
17 Ashcombe Lane, West Perth

```html
<!DOCTYPE html>
<html lang="en">
<head>
<meta charset="utf-8">
<title>Lumora Dwellings – Business Card</title>
<link rel="stylesheet" href="https://fonts.googleapis.com/css2?family=Jura:wght@500;600;700&display=swap">
<style>
  :root {
    --backdrop: #e4e6e8;
    --card-aqua: #bfe5ef;
    --card-aqua-muted: #aed6de;
    --band: #050505;
    --brand-blue: #3aa9cf;
    --tagline: #e8e8e8;
    --ink: #101418;
  }
  * { box-sizing: border-box; margin: 0; padding: 0; }
  html, body {
    width: 1200px;
    height: 534px;
    overflow: hidden;
    background: var(--backdrop);
    font-family: "Jura", sans-serif;
  }
  .stage {
    position: relative;
    width: 1200px;
    height: 534px;
  }
  .card {
    position: absolute;
    top: 119px;
    width: 517px;
    height: 293px;
    background: var(--card-aqua);
    color: var(--ink);
  }
  .card--rounded { left: 62px; border-radius: 14px; }
  .card--square { left: 621px; background: var(--card-aqua-muted); }
  .brand-band {
    position: absolute;
    top: 51px;
    left: 0;
    width: 100%;
    height: 127px;
    background: var(--band);
  }
  .brand-tagline {
    position: absolute;
    top: 37px;
    left: 226px;
    font-size: 11.5px;
    font-weight: 500;
    color: var(--tagline);
    white-space: nowrap;
  }
  .brand-lockup {
    position: absolute;
    top: 59px;
    left: 0;
    width: 100%;
    display: flex;
    justify-content: center;
    align-items: center;
    gap: 12px;
  }
  .brand-mark {
    width: 21px;
    height: 21px;
    background: var(--brand-blue);
  }
  .brand-name {
    font-size: 28px;
    font-weight: 700;
    letter-spacing: 1px;
    color: var(--brand-blue);
    text-transform: uppercase;
    white-space: nowrap;
  }
  .contact {
    position: absolute;
    top: 205px;
    left: 0;
    width: 100%;
    text-align: center;
    text-transform: uppercase;
    font-weight: 600;
  }
  .contact-name {
    font-size: 15px;
    letter-spacing: 0.5px;
    margin-bottom: 9px;
  }
  .contact-role { font-size: 11px; }
  .contact-line {
    font-size: 11px;
    letter-spacing: 0.3px;
    line-height: 20px;
  }
</style>
</head>
<body>
<main class="stage">
  <article class="card card--rounded">
    <div class="brand-band">
      <p class="brand-tagline">Smarter Living At Your Fingertip</p>
      <div class="brand-lockup">
        <span class="brand-mark"></span>
        <span class="brand-name">Lumora Dwellings</span>
      </div>
    </div>
    <div class="contact">
      <p class="contact-name">Tobias Fenwright // <span class="contact-role">Director</span></p>
      <p class="contact-line">Phone: 0471596234 &nbsp;// &nbsp;Address: 17 Ashcombe Lane, West Perth</p>
      <p class="contact-line">Website: www.lumoradwellings.com.au</p>
    </div>
  </article>

  <article class="card card--square">
    <div class="brand-band">
      <p class="brand-tagline">Smarter Living At Your Fingertip</p>
      <div class="brand-lockup">
        <span class="brand-mark"></span>
        <span class="brand-name">Lumora Dwellings</span>
      </div>
    </div>
    <div class="contact">
      <p class="contact-name">Tobias Fenwright // <span class="contact-role">Director</span></p>
      <p class="contact-line">Phone: 0471596234 &nbsp;// &nbsp;Address: 17 Ashcombe Lane, West Perth</p>
      <p class="contact-line">Website: www.lumoradwellings.com.au</p>
    </div>
  </article>
</main>
</body>
</html>
```